Web Developer Needs a Business Card Design

I need a personal business card design that represents me as a web developer for potential employers. I would like the background to be a dark color on the front for contrast with my logo and name. The back will have all my information along with a smaller version of the logo. I want something with a modern look and feel, not too conservative. This will be used for potential employers and freelance work.

Industry/Entity Type

Business

Contact Information for Business Card

Front should have my logo and name. The back should have all my personal information which would include: name: Tom Brevardi, phone: 570-614-9083, email: tombrevardi@mailwisp.com, website url: www.tombrevardi.com, logo, web developer.

Font styles to use
Sans Serif

Requirements
Must have
• Must include my logo. The color palette base color will be the logo color.

```html
<!DOCTYPE html>
<html lang="en">
<head>
<meta charset="utf-8">
<title>Tom Brevardi — Business Card</title>
<link href="https://fonts.googleapis.com/css2?family=Questrial&display=swap" rel="stylesheet">
<style>
  :root {
    --bg: #8c8e8d;
    --teal: #4ecba8;
    --card-dark: #141615;
    --card-dark-2: #1a201e;
    --card-light: #ececec;
    --ink: #6d6d6d;
    --rule: #9a9a9a;
  }
  * { margin: 0; padding: 0; box-sizing: border-box; }
  html, body { width: 1200px; height: 900px; overflow: hidden; }
  body {
    background: var(--bg);
    font-family: "Questrial", "Century Gothic", sans-serif;
    position: relative;
  }
  .card {
    position: absolute;
    left: 321px;
    width: 507px;
    height: 290px;
  }
  .card-front { top: 119px; background: var(--card-dark); }
  .card-back { top: 470px; background: var(--card-light); }

  .front-texture {
    position: absolute; inset: 0;
    background: radial-gradient(ellipse at center, var(--card-dark-2) 0%, var(--card-dark) 80%);
  }
  .front-mark {
    position: absolute; left: 0; right: 0; top: 0; bottom: 0;
    display: flex; align-items: center; justify-content: center; gap: 14px;
  }
  .mark-circle {
    width: 30px; height: 30px; border-radius: 50%;
    border: 3px solid var(--teal);
  }
  .mark-name { color: var(--teal); font-size: 30px; letter-spacing: 0.5px; }

  .back-mark {
    position: absolute; right: 30px; top: 22px;
    display: flex; flex-direction: column; align-items: center; gap: 10px;
  }
  .back-mark .mark-circle { width: 70px; height: 70px; border-width: 5px; }
  .back-mark .mark-name { font-size: 17px; }

  .holder-name {
    position: absolute; left: 28px; top: 155px;
    color: var(--teal); font-size: 25px; letter-spacing: 0.3px;
  }
  .holder-title {
    position: absolute; left: 28px; top: 192px; right: 31px;
    display: flex; align-items: center; gap: 3px;
    color: var(--ink); font-size: 15px;
  }
  .holder-title .rule { flex: 1; height: 1px; background: var(--rule); margin-top: 6px; }

  .contact-list {
    position: absolute; left: 28px; top: 224px;
    list-style: none; color: var(--ink); font-size: 13.5px;
  }
  .contact-list li { display: flex; align-items: center; gap: 7px; height: 19.5px; }
  .contact-list svg { width: 12px; height: 12px; fill: var(--teal); }

  .social-list {
    position: absolute; right: 31px; top: 250px;
    list-style: none; display: flex; gap: 8px;
  }
  .social-list li { display: flex; align-items: center; gap: 3px; color: var(--teal); font-size: 10px; }
  .social-list .dot { width: 10px; height: 10px; border-radius: 50%; border: 1.5px solid var(--teal); }
</style>
</head>
<body>
  <section class="card card-front">
    <div class="front-texture" role="img" aria-label="Dark repeating monogram pattern in muted teal"></div>
    <div class="front-mark">
      <span class="mark-circle"></span>
      <span class="mark-name">Tom Brevardi</span>
    </div>
  </section>

  <section class="card card-back">
    <div class="back-mark">
      <span class="mark-circle"></span>
      <span class="mark-name">Tom Brevardi</span>
    </div>

    <h1 class="holder-name">Tom Brevardi</h1>
    <p class="holder-title"><span>Front-End Developer</span><span class="rule"></span></p>

    <ul class="contact-list">
      <li>
        <svg viewBox="0 0 24 24"><path d="M6.6 10.8a15.1 15.1 0 0 0 6.6 6.6l2.2-2.2c.3-.3.7-.4 1-.2 1.1.4 2.3.6 3.6.6.6 0 1 .4 1 1V20c0 .6-.4 1-1 1A17 17 0 0 1 3 4c0-.6.4-1 1-1h3.5c.6 0 1 .4 1 1 0 1.3.2 2.5.6 3.6.1.3 0 .7-.2 1z"/></svg>
        <span>570-614-9083</span>
      </li>
      <li>
        <svg viewBox="0 0 24 24"><path d="M2 5h20v14H2zm2 2v.5l8 5 8-5V7l-8 5z"/></svg>
        <span>tombrevardi@mailwisp.com</span>
      </li>
      <li>
        <svg viewBox="0 0 24 24"><circle cx="12" cy="12" r="10"/></svg>
        <span>www.tombrevardi.com</span>
      </li>
    </ul>

    <ul class="social-list">
      <li><span class="dot"></span>Chirply</li>
      <li><span class="dot"></span>Linkfolio</li>
      <li><span class="dot"></span>Codevault</li>
    </ul>
  </section>
</body>
</html>
```